Property Development Business Cards

I need a business card design for Tallow Creek Developments Pty Ltd. We are a property development company in Australia and our name defines the five values that we adhere to, being Profitable, Partnerships, Quality Developments, Eco Friendly and Enduring Design.

I have attached the current logo that I use, it is just five yellow circles connected to a single cricle in the middle.

Target Market(s)

Our Target audience is real estate agents, owners of properties, builders and other trades

Industry/Entity Type

Business

Requirements
Must have
• Want to have two sides to the card, one with details and one to just highlight the company

```html
<!DOCTYPE html>
<html lang="en">
<head>
<meta charset="utf-8">
<title>Tallow Creek Developments – Business Card</title>
<link rel="stylesheet" href="https://fonts.googleapis.com/css2?family=Arimo:wght@400;700&display=swap">
<style>
  :root {
    --backdrop: #ececec;
    --card: #ffffff;
    --ink: #4a4a4a;
    --ink-soft: #555555;
    --gold: #edb22c;
    --on-gold: #ffffff;
  }
  * { margin: 0; padding: 0; box-sizing: border-box; }
  html, body {
    width: 1200px;
    height: 818px;
    overflow: hidden;
    background: var(--backdrop);
    font-family: "Arimo", Arial, sans-serif;
  }
  .business-card {
    position: absolute;
    left: 159px;
    top: 159px;
    width: 870px;
    height: 497px;
    background: var(--card);
    box-shadow: 0 4px 14px rgba(0, 0, 0, 0.18);
  }
  .brand {
    position: absolute;
    left: 128px;
    top: 70px;
    display: flex;
    align-items: center;
    gap: 133px;
  }
  .brand-dot {
    width: 80px;
    height: 80px;
    border-radius: 50%;
    background: var(--gold);
    flex: none;
  }
  .brand-name {
    font-weight: 700;
    font-size: 60px;
    line-height: 58px;
    letter-spacing: -0.8px;
    color: var(--ink);
  }
  .contact-name {
    position: absolute;
    left: 0;
    right: 0;
    top: 232px;
    text-align: center;
    font-weight: 700;
    font-size: 30px;
    line-height: 34px;
    color: var(--ink);
  }
  .contact-details {
    position: absolute;
    left: 0;
    right: 0;
    top: 303px;
    text-align: center;
    color: var(--ink-soft);
  }
  .contact-line {
    font-size: 26px;
    line-height: 42px;
    letter-spacing: -0.5px;
  }
  .web-band {
    position: absolute;
    left: 0;
    right: 0;
    bottom: 0;
    height: 86px;
    background: var(--gold);
    display: flex;
    align-items: center;
    justify-content: center;
  }
  .web-address {
    font-weight: 700;
    font-size: 31px;
    color: var(--on-gold);
    letter-spacing: -0.3px;
  }
</style>
</head>
<body>
  <main class="business-card">
    <header class="brand">
      <span class="brand-dot" aria-hidden="true"></span>
      <h1 class="brand-name">Tallow Creek<br>Developments</h1>
    </header>
    <p class="contact-name">Daniel Marsh</p>
    <section class="contact-details">
      <p class="contact-line">0412 555 318 &nbsp;| Daniel@TallowCreekDevelopments.com.au</p>
      <p class="contact-line">PO Box 218 | Hume, ACT 2620</p>
    </section>
    <footer class="web-band">
      <p class="web-address">www.tallowcreekdevelopments.com.au</p>
    </footer>
  </main>
</body>
</html>
```